Defend science flier

Put my name and text below on one side of flier, and place other text on other side. Try to keep file about 4 by 6 or 6 by 8 inches.

Target Market(s)

Community and retailers.

Industry/Entity Type

Retail and concerned community.

Font styles to use
Serif

Requirements
Must have
• Good, eye-catching titles. Be smaller format. Not 8 by 11
Nice to have
• Black and white text. Maybe bullets etc for organizion but no decorations.
Should not have
• Any decoration

```html
<!DOCTYPE html>
<html lang="en">
<head>
<meta charset="utf-8">
<title>Defend Science Flier</title>
<link rel="stylesheet" href="https://fonts.googleapis.com/css2?family=Tinos:ital,wght@0,400;0,700;1,400;1,700&display=swap">
<style>
  :root {
    --gold: #ad8c4e;
    --cream: #f6f3e1;
    --ink: #1d1d1d;
    --paper: #ffffff;
    --grey: #a7a7a9;
    --bg: #ffffff;
  }
  * { box-sizing: border-box; margin: 0; padding: 0; }
  html, body { width: 1200px; height: 4000px; overflow: hidden; background: var(--bg); }
  body { font-family: "Tinos", "Times New Roman", serif; color: var(--ink); position: relative; }

  .card {
    position: absolute; left: 152px; width: 896px;
    background: var(--paper);
    box-shadow: 0 4px 14px rgba(0,0,0,0.12);
  }
  .card--front { top: 626px; height: 1341px; }
  .card--back { top: 2027px; height: 1347px; }

  .card__band { position: absolute; left: 0; top: 0; width: 100%; background: var(--gold); }
  .card--front .card__band { height: 146px; }
  .card--back .card__band { height: 400px; }

  .card__footer { position: absolute; left: 0; bottom: 0; width: 100%; height: 12px; display: block; }

  .header-box {
    position: absolute; left: 54px; width: 788px;
    background: var(--cream);
    border: 3px solid var(--gold);
    border-radius: 18px;
    box-shadow: 0 0 0 9px var(--paper);
  }
  .card--front .header-box { top: 56px; height: 245px; text-align: center; padding-top: 34px; }
  .card--back .header-box { top: 57px; height: 540px; padding: 22px 60px 0 30px; }

  .name { font-size: 58px; font-weight: 400; line-height: 1.1; }
  .tagline { font-size: 28px; margin-top: 8px; }
  .ornament {
    display: block; width: 458px; height: 37px; margin: 14px auto 0;
    background: linear-gradient(90deg, #f2f0ea, #bdbab4 50%, #f2f0ea);
  }

  .content { position: absolute; left: 54px; right: 54px; }
  .card--front .content { top: 338px; }
  .card--back .content { top: 640px; }

  .lead, .body-copy { font-size: 35px; line-height: 1.28; }
  .ruled { border-left: 5px solid var(--gold); padding-left: 20px; margin-left: 6px; }
  .lead { text-align: justify; }
  .body-copy + .body-copy { margin-top: 12px; }
  .lead + .body-copy { margin-top: 14px; }

  .quote {
    position: relative; margin: 28px 8px 0 12px; height: 388px;
    border: 3px solid var(--gold); border-radius: 22px;
    background: var(--paper);
    padding: 44px 26px 0 66px;
    font-size: 35px; line-height: 1.29;
  }
  .quote__mark { position: absolute; color: var(--gold); font-weight: 700; font-size: 82px; line-height: 1; }
  .quote__mark--open { left: 14px; top: 14px; }
  .quote__mark--close { position: relative; font-size: 82px; top: 34px; margin-left: 34px; line-height: 0; }

  .cta { text-align: center; font-size: 37px; font-weight: 700; margin-top: 34px; }
  .url {
    display: block; width: 492px; height: 62px; margin: 16px auto 0;
    background: var(--gold); color: var(--paper); border-radius: 14px;
    font-size: 40px; line-height: 62px; text-align: center;
  }

  .title { font-size: 47px; font-weight: 700; line-height: 1.2; }
  .vice-list { list-style: none; margin-top: 10px; }
  .vice-list li {
    position: relative; padding-left: 68px; font-size: 30px; line-height: 1.27; margin-top: 30px;
  }
  .vice-list li:first-child { margin-top: 20px; }
  .vice-num {
    position: absolute; left: 6px; top: 0; width: 42px; height: 42px; border-radius: 50%;
    background: var(--gold); color: var(--paper); font-size: 20px; line-height: 42px; text-align: center;
  }

  .argument { font-size: 35px; line-height: 1.26; }
  .argument + .argument { margin-top: 56px; }
</style>
</head>
<body>

<article class="card card--front">
  <div class="card__band"></div>
  <header class="header-box">
    <h1 class="name">Martin R. Halvorsen, Ph.D.</h1>
    <p class="tagline">“The Pioneer and Visionary of Psychology and History”</p>
    <span class="ornament" role="img" aria-label="Decorative scroll ornament"></span>
  </header>
  <div class="content">
    <p class="lead ruled">Martin’s Bio-Psych has Restructured the Liberal Arts and Sciences—<em>from <strong>Genetics to the Fine Arts and Hollywood.</strong></em></p>
    <p class="body-copy">Museum Catalogues, Better Nonfiction, and Hollywood Films Now Use <strong>Martin’s Methods.</strong></p>
    <p class="body-copy">Martin’s Biopsych is endorsed by <strong>Dr. E. Conrad Whitfield,</strong> professor of psychiatry at Northbridge Medical School, who said:</p>
    <blockquote class="quote">
      <span class="quote__mark quote__mark--open">“</span>
      Modern sleep and dream research teaches us—as does <strong><em>Martin Halvorsen’s book Nature’s Sin or Social Sin</em></strong>—that all human activities, including art and politics, are products of the human brain, and that each of us has the privilege and responsibility of using it and communicating its creations.<span class="quote__mark quote__mark--close">”</span>
    </blockquote>
    <p class="cta">See Martin’s homepage for more details:</p>
    <span class="url">www.martin-halvorsen.org</span>
  </div>
  <svg class="card__footer" viewBox="0 0 896 12" preserveAspectRatio="none" aria-hidden="true">
    <polygon points="0,0 402,0 414,12 0,12" fill="#ad8c4e"/>
    <polygon points="410,0 896,0 896,12 422,12" fill="#a7a7a9"/>
  </svg>
</article>

<article class="card card--back">
  <div class="card__band"></div>
  <section class="header-box">
    <h2 class="title">Why Did the Culture Change?</h2>
    <ol class="vice-list">
      <li><span class="vice-num">01</span>Pride became <strong>“Racism.”</strong></li>
      <li><span class="vice-num">02</span>Lust became <strong>“Sexism”</strong> and <strong>“Gender“</strong> existing <strong>“out there.”</strong></li>
      <li><span class="vice-num">03</span>Gluttony became <strong>“Consumer Fetishism.”</strong></li>
      <li><span class="vice-num">04</span>Vanity became <strong>“Media Images of Beauty.”</strong></li>
      <li><span class="vice-num">05</span>Sloth became The lack of social action: <strong>“Are you fighting for diversity?”</strong></li>
    </ol>
  </section>
  <div class="content">
    <p class="argument ruled">This <strong>“fight for diversity”</strong> inspires attacks against people like Dr. Halvorsen for asserting any reality principle about human nature.</p>
    <p class="argument ruled">These thugs are religious crusaders who ignore the rule of law and try to stop the progress of science. These fanatics go around and give people a <strong>“tear-test”</strong>—as during the Salem witch trials. Don’t let them take over.</p>
    <p class="argument ruled">The educational and culture elites—such as Hollywood—now reject these theological <strong>“social sins.”</strong> The elites are replacing theology with traditional, human-based sin.</p>
  </div>
  <svg class="card__footer" viewBox="0 0 896 12" preserveAspectRatio="none" aria-hidden="true">
    <polygon points="0,0 402,0 414,12 0,12" fill="#ad8c4e"/>
    <polygon points="410,0 896,0 896,12 422,12" fill="#a7a7a9"/>
  </svg>
</article>

</body>
</html>
```